Oaths and Harbors (Book cover needed)

Oaths and Harbors: Notes from a Career in Civic Work

Author: Perla Winthrop Okonedo

Foreword by Ambassador Delphine R. Osei

Book Trim Size: 5.5 x 8.5

```html
<!DOCTYPE html>
<html lang="en">
<head>
<meta charset="utf-8">
<title>Oaths and Harbors — Book Cover</title>
<link rel="stylesheet" href="https://fonts.googleapis.com/css2?family=Anton&family=Montserrat:wght@500;600;700;800&display=swap">
<style>
  :root {
    --cover-bg: #1c1f27;
    --title-ink: #d9d9da;
    --text-ink: #e6e6e8;
    --portrait-top: #b8232c;
    --portrait-skin: #7d4d36;
    --portrait-dress-red: #8f1c26;
    --portrait-dress-dark: #2b1c22;
  }
  html, body {
    margin: 0;
    padding: 0;
    width: 777px;
    height: 1200px;
    overflow: hidden;
    background: var(--cover-bg);
  }
  .cover {
    position: relative;
    width: 777px;
    height: 1200px;
    background: var(--cover-bg);
    overflow: hidden;
  }
  .cover-art, .cover-type {
    position: absolute;
    inset: 0;
    width: 777px;
    height: 1200px;
  }
  .title-word {
    font-family: "Anton", "Impact", sans-serif;
    fill: var(--title-ink);
  }
  .title-joiner {
    font-family: "Montserrat", sans-serif;
    font-weight: 800;
    font-size: 46px;
    fill: var(--title-ink);
  }
  .joiner-rule {
    stroke: var(--title-ink);
    stroke-width: 3;
  }
  .subtitle {
    font-family: "Montserrat", sans-serif;
    font-weight: 500;
    font-size: 22px;
    letter-spacing: 0.5px;
    fill: var(--text-ink);
  }
  .author-name {
    font-family: "Montserrat", sans-serif;
    font-weight: 700;
    font-size: 35px;
    fill: var(--text-ink);
  }
  .foreword-label {
    font-family: "Montserrat", sans-serif;
    font-weight: 500;
    font-size: 19px;
    fill: var(--text-ink);
  }
  .foreword-name {
    font-family: "Montserrat", sans-serif;
    font-weight: 700;
    font-size: 36px;
    fill: var(--text-ink);
  }
</style>
</head>
<body>
  <main class="cover">
    <svg class="cover-art" viewBox="0 0 777 1200" role="img" aria-label="Portrait photograph of the author, smiling, wearing a red head wrap and a red and black patterned dress">
      <defs>
        <linearGradient id="portraitTone" x1="0" y1="0" x2="0.35" y2="1">
          <stop offset="0" stop-color="var(--portrait-top)"/>
          <stop offset="0.14" stop-color="var(--portrait-top)"/>
          <stop offset="0.24" stop-color="var(--portrait-skin)"/>
          <stop offset="0.44" stop-color="var(--portrait-skin)"/>
          <stop offset="0.56" stop-color="var(--portrait-dress-red)"/>
          <stop offset="1" stop-color="var(--portrait-dress-dark)"/>
        </linearGradient>
      </defs>
      <path fill="url(#portraitTone)" d="M0,92 C70,68 200,72 236,150 L238,300 C232,400 205,470 262,525 C400,520 545,580 590,720 C600,800 585,900 560,1000 L545,1200 L0,1200 Z"/>
    </svg>

    <svg class="cover-type" viewBox="0 0 777 1200">
      <text class="title-word" x="730" y="268" font-size="215" text-anchor="end" textLength="443" lengthAdjust="spacingAndGlyphs">OATHS</text>

      <line class="joiner-rule" x1="381" y1="326" x2="427" y2="326"/>
      <text class="title-joiner" x="497" y="342" text-anchor="middle" textLength="117" lengthAdjust="spacingAndGlyphs">AND</text>
      <line class="joiner-rule" x1="571" y1="326" x2="618" y2="326"/>

      <text class="title-word" x="730" y="462" font-size="126" text-anchor="end" textLength="441" lengthAdjust="spacingAndGlyphs">HARBORS</text>

      <text class="subtitle" text-anchor="end">
        <tspan x="730" y="619">NOTES FROM</tspan>
        <tspan x="730" y="649">A CAREER IN</tspan>
        <tspan x="730" y="679">CIVIC WORK</tspan>
      </text>

      <text class="author-name" x="730" y="1049" text-anchor="end" textLength="512" lengthAdjust="spacingAndGlyphs">PERLA WINTHROP OKONEDO</text>

      <text class="foreword-label" x="730" y="1084" text-anchor="end">FOREWORD BY</text>
      <text class="foreword-name" x="730" y="1119" text-anchor="end" textLength="221" lengthAdjust="spacingAndGlyphs">AMBASSADOR</text>
      <text class="foreword-name" x="730" y="1154" text-anchor="end" textLength="314" lengthAdjust="spacingAndGlyphs">DELPHINE R. OSEI</text>
    </svg>
  </main>
</body>
</html>
```